Business Card Design Project

Hi,

We are a new modern sheet metal business and I require a business card for our sales reps.

The card should be double sided and standout in a crowd.

I have attached our logo and our website is www.plyform.com.au.

Please ask if you have any further questions
Updates

hi everyone, 

I'm wondering if we can try to lighten the cards mood.  Everyone is using black and I'm not sure how that would be accepted in real life.

Gordon

Reason: Still No receiving what I was hoping for.

Industry/Entity Type

Business

Requirements
Must have
• double sided

```html
<!DOCTYPE html>
<html lang="en">
<head>
<meta charset="utf-8">
<title>Plyform Sheetmetal – Business Card, Front and Back</title>
<link rel="stylesheet" href="https://fonts.googleapis.com/css2?family=Open+Sans:wght@600;700;800&family=Playfair+Display:wght@800&display=swap">
<style>
  :root {
    --stage: #e4e4e4;
    --card-dark: #262a2b;
    --card-white: #ffffff;
    --panel-dark: #2f2d2e;
    --accent-red: #ee3237;
    --navy: #2e3192;
    --cyan: #1aa7e1;
    --lime: #b4cc3a;
    --faint-text: #d3d7de;
    --bullet: #b9b9b9;
    --ink-dark: #2a2a2a;
    --white: #ffffff;
  }
  * { box-sizing: border-box; margin: 0; padding: 0; }
  html, body { width: 1200px; height: 901px; overflow: hidden; }
  body {
    background: var(--stage);
    font-family: "Open Sans", Arial, sans-serif;
    position: relative;
  }
  .card {
    position: absolute;
    top: 305px;
    width: 500px;
    height: 290px;
    overflow: hidden;
    box-shadow: 0 6px 18px rgba(0,0,0,.18);
  }

  /* Back side */
  .card--back { left: 70px; background: var(--card-dark); }
  .back__title {
    position: absolute; top: 30px; left: 0; width: 100%;
    text-align: center;
    font-family: "Playfair Display", Georgia, serif;
    font-weight: 800; font-size: 26px; letter-spacing: .5px;
    color: var(--white);
    text-decoration: underline; text-underline-offset: 5px;
  }
  .details { position: absolute; top: 95px; list-style: none; }
  .details--left { left: 34px; }
  .details--right { left: 272px; }
  .details li { display: flex; align-items: center; gap: 14px; height: 36px; }
  .details .dot {
    width: 14px; height: 14px; border-radius: 50%;
    background: radial-gradient(circle at 35% 35%, #f2f2f2, var(--bullet) 60%, #7d7d7d);
  }
  .details .line { width: 160px; height: 0; border-bottom: 3px dotted var(--white); }
  .service-band { position: absolute; left: 0; bottom: 0; width: 500px; height: 46px; }
  .service-band text {
    font-family: "Open Sans", Arial, sans-serif;
    font-weight: 700; font-size: 19px; fill: var(--white);
  }

  /* Front side */
  .card--front { left: 630px; background: var(--card-white); }
  .front__services {
    position: absolute; left: 22px; bottom: 30px;
    font-size: 22px; font-weight: 600;
    color: var(--faint-text);
    word-spacing: 4px;
    white-space: nowrap;
  }
  .name-panel {
    position: absolute;
    left: -5px; top: -10px;          /* centre at 115,110 */
    width: 240px; height: 240px;
    background: var(--panel-dark);
    border-top-left-radius: 22px;
    transform: rotate(-28deg);
  }
  .brand {
    position: absolute; left: 0; top: 36px; width: 100%;
    display: flex; align-items: center; justify-content: center; gap: 8px;
  }
  .brand__mark { width: 14px; height: 14px; background: var(--navy); }
  .brand__name { font-weight: 800; font-size: 26px; color: var(--white); letter-spacing: 1px; }
  .name-panel__name {
    position: absolute; left: 0; top: 148px; width: 100%;
    text-align: center;
    font-family: "Playfair Display", Georgia, serif;
    font-weight: 800; font-size: 30px; color: var(--white);
    text-decoration: underline; text-underline-offset: 5px;
  }
  .contact-panel {
    position: absolute;
    left: 290px; top: 110px;         /* centre at 405,225 */
    width: 230px; height: 230px;
    background: var(--accent-red);
    border-radius: 0 0 24px 0;
    transform: rotate(-28deg);
    padding: 26px 0 0 28px;
  }
  .contact-panel p {
    font-weight: 800; font-size: 16px; color: var(--ink-dark);
    line-height: 22px;
  }
  .contact-panel .gap { margin-top: 22px; }
</style>
</head>
<body>

  <section class="card card--back" aria-label="Card back">
    <h2 class="back__title">OTHER DETALS</h2>
    <ul class="details details--left">
      <li><span class="dot"></span><span class="line"></span></li>
      <li><span class="dot"></span><span class="line"></span></li>
      <li><span class="dot"></span><span class="line"></span></li>
      <li><span class="dot"></span><span class="line"></span></li>
    </ul>
    <ul class="details details--right">
      <li><span class="dot"></span><span class="line"></span></li>
      <li><span class="dot"></span><span class="line"></span></li>
      <li><span class="dot"></span><span class="line"></span></li>
      <li><span class="dot"></span><span class="line"></span></li>
    </ul>
    <svg class="service-band" viewBox="0 0 500 46" aria-label="Services">
      <polygon points="0,0 150,0 130,46 0,46" fill="var(--navy)"/>
      <polygon points="150,0 270,0 250,46 130,46" fill="var(--cyan)"/>
      <polygon points="270,0 500,0 500,46 250,46" fill="var(--lime)"/>
      <text x="18" y="30">Flashings</text>
      <text x="162" y="30">Gutter</text>
      <text x="288" y="30">Rainwater Good</text>
    </svg>
  </section>

  <section class="card card--front" aria-label="Card front">
    <p class="front__services">Flashings | Gutter | Rainwater Good</p>

    <div class="name-panel">
      <div class="brand">
        <span class="brand__mark"></span>
        <span class="brand__name">PLYFORM</span>
      </div>
      <h1 class="name-panel__name">NAME</h1>
    </div>

    <div class="contact-panel">
      <p>ADD.</p>
      <p class="gap">Wab.-</p>
      <p>E-mail-</p>
      <p>Mob.-</p>
    </div>
  </section>

</body>
</html>
```